Labelling needed for New 18L Paint Tub *

Looking to obtain new label on our new line of our 18L paint tubs (cylindrical shape).

We have attached a "design template contents" word doc which contains all of the wording and descriptions our label needs. It has been colour coded to reflect that the descriptions in those colours should stay together.

We have also attached an image of our competitors design which we would like to create a similar style.

The other file attached is our logo

Target Market(s)

Tradesman, Painters, DIY handymen,

Industry/Entity Type

Paint

Font styles to use
Sans Serif

Colors

Designer to choose colors to be used in the design.

Requirements
Must have
• Company Logo

```html
<!DOCTYPE html>
<html lang="en">
<head>
<meta charset="utf-8">
<title>KELDA 18L Low Sheen White Label</title>
<link href="https://fonts.googleapis.com/css2?family=Open+Sans:wght@400;600;700&family=Noto+Serif:wght@400;700&display=swap" rel="stylesheet">
<style>
  :root {
    --bg: #6690b0;
    --band: #f7941d;
    --band-text: #ffffff;
    --paper: #ffffff;
    --ink: #111111;
    --rule: #7a7a7a;
    --heading-blue: #1b75bc;
    --heading-pink: #d6247a;
    --heading-orange: #f7941d;
    --note-pink: #e6007e;
    --warn-red: #e3242b;
    --wash: rgba(220, 200, 210, 0.25);
  }
  * { box-sizing: border-box; margin: 0; padding: 0; }
  html, body { width: 1143px; height: 1200px; overflow: hidden; }
  body { background: var(--bg); position: relative; font-family: "Noto Serif", serif; color: var(--ink); }

  .label { position: absolute; left: 36px; top: 321px; width: 1072px; height: 557px; background: var(--paper); }
  .band { position: absolute; left: 0; width: 100%; height: 40px; background: var(--band); display: flex; }
  .band--top { top: 0; }
  .band--bottom { bottom: 0; height: 41px; }
  .band__cell { font-family: "Open Sans", sans-serif; font-weight: 700; color: var(--band-text); font-size: 16px; display: flex; align-items: center; gap: 24px; padding-left: 38px; }
  .band__cell:nth-child(1) { width: 384px; }
  .band__cell:nth-child(2) { width: 372px; padding-left: 43px; }
  .band__cell:nth-child(3) { width: 316px; padding-left: 56px; }
  .band__cell span:last-child { margin-left: 8px; }

  .body { position: absolute; top: 40px; left: 0; width: 100%; height: 476px; display: flex; }
  .col { position: relative; height: 100%; border-right: 1px solid var(--rule); }
  .col:last-child { border-right: none; }
  .col--left { width: 384px; }
  .col--mid { width: 372px; }
  .col--right { width: 316px; }
  .panel { position: relative; border-bottom: 1px solid var(--rule); overflow: hidden; }
  .panel:last-child { border-bottom: none; }

  .wash { position: absolute; inset: 0; background: radial-gradient(ellipse at 55% 60%, var(--wash), rgba(255,255,255,0) 70%); pointer-events: none; }

  .brand { height: 112px; display: flex; align-items: center; padding-left: 34px; gap: 14px; }
  .brand__dot { width: 40px; height: 40px; border-radius: 50%; background: var(--heading-blue); }
  .brand__name { font-family: "Open Sans", sans-serif; font-weight: 600; font-size: 50px; letter-spacing: 1px; }

  .description { height: 146px; padding: 26px 24px 0 24px; }
  h2 { font-weight: 700; line-height: 1.1; }
  .h-pink { color: var(--heading-pink); font-size: 16px; margin-bottom: 8px; }
  .h-orange { color: var(--heading-orange); font-size: 22px; }
  .h-blue { color: var(--heading-blue); font-size: 22px; text-align: center; }
  .description p { font-size: 11.2px; line-height: 1.32; position: relative; }

  .features { height: 218px; padding: 8px 24px 0 24px; }
  .feature-grid { display: grid; grid-template-columns: 181px 1fr; row-gap: 15px; margin-top: 12px; position: relative; }
  .feature { display: flex; align-items: center; gap: 10px; font-family: "Open Sans", sans-serif; font-size: 9px; }
  .feature svg { width: 20px; height: 20px; flex: none; }

  .tools { height: 164px; padding-top: 24px; }
  .tool-row { position: relative; height: 100px; }
  .tool { position: absolute; display: flex; align-items: center; gap: 6px; font-family: "Open Sans", sans-serif; font-weight: 600; font-size: 11px; }
  .tool svg { width: 34px; height: 34px; }

  .condition { height: 105px; padding-top: 4px; }
  .condition p { font-size: 10px; line-height: 1.3; padding: 10px 44px 0 70px; position: relative; }

  .instructions { height: 207px; padding-top: 3px; }
  .steps { list-style: none; font-size: 10px; line-height: 1.18; padding: 8px 30px 0 48px; position: relative; }
  .remarks { font-size: 6.5px; line-height: 1.3; padding: 8px 30px 0 68px; position: relative; }

  .care { height: 239px; padding: 24px 28px 0 32px; font-family: "Open Sans", sans-serif; font-size: 8.4px; line-height: 1.25; }
  .care h3, .safety h3 { font-weight: 400; color: var(--note-pink); font-size: 8.4px; margin-top: 8px; }
  .care h3:first-child { margin-top: 0; }
  .care p, .safety p { position: relative; }
  .care .warn { color: var(--warn-red); font-size: 6px; text-align: center; margin-top: 10px; }

  .safety { height: 237px; padding: 18px 14px 0 14px; font-family: "Open Sans", sans-serif; font-size: 6.4px; line-height: 1.3; }
  .safety h2 { color: var(--heading-blue); font-family: "Noto Serif", serif; font-size: 11px; margin-bottom: 10px; }
  .safety h3 { font-size: 6.4px; margin-top: 8px; }
  .safety .warn { color: var(--warn-red); font-weight: 700; font-size: 7px; margin-top: 14px; }
</style>
</head>
<body>
<main class="label">
  <header class="band band--top">
    <div class="band__cell"><span>Low Sheen</span><span>White</span><span>18L</span></div>
    <div class="band__cell"><span>Low Sheen</span><span>White</span><span>18L</span></div>
    <div class="band__cell"><span>Low Sheen</span><span>White</span><span>18L</span></div>
  </header>

  <div class="body">
    <section class="col col--left">
      <div class="panel brand">
        <span class="brand__dot"></span>
        <span class="brand__name">KELDA</span>
      </div>
      <div class="panel description">
        <div class="wash" role="img" aria-label="Faint decorative background pattern"></div>
        <h2 class="h-pink">Product Description</h2>
        <p>A premium, eco-friendly, water-based paint for interior ceiling and wall application.<br>KELDA's TradeLine line delivers the high quality results that professionals love whilst maintaining the lowest levels of odour emissions and VOC content.</p>
      </div>
      <div class="panel features">
        <div class="wash" role="img" aria-label="Faint decorative background pattern"></div>
        <h2 class="h-orange">Features</h2>
        <div class="feature-grid">
          <div class="feature"><svg viewBox="0 0 20 20"><circle cx="10" cy="10" r="8.5" fill="none" stroke="#111" stroke-width="1.6"/><circle cx="10" cy="10" r="3" fill="#111"/></svg>Low VOC content</div>
          <div class="feature"><svg viewBox="0 0 20 20"><circle cx="10" cy="10" r="9.5" fill="#111"/><path d="M10 4 C7 8 6 10 6 12 a4 4 0 0 0 8 0 C14 10 13 8 10 4Z" fill="#fff"/></svg>Water-Washable</div>
          <div class="feature"><svg viewBox="0 0 20 20"><circle cx="10" cy="10" r="9.5" fill="#111"/><path d="M6 6 L14 14 M14 6 L6 14" stroke="#fff" stroke-width="1.6"/></svg>Low Odor levels</div>
          <div class="feature"><svg viewBox="0 0 20 20"><circle cx="10" cy="10" r="9.5" fill="#111"/><rect x="7" y="5" width="6" height="5" fill="#fff"/><rect x="9" y="10" width="2" height="5" fill="#fff"/></svg>Self-Priming</div>
          <div class="feature"><svg viewBox="0 0 20 20"><circle cx="10" cy="10" r="8.5" fill="none" stroke="#111" stroke-width="1.6"/><path d="M6 10 L9 13 L14 7" fill="none" stroke="#111" stroke-width="1.8"/></svg>Super Adhesiveness</div>
          <div class="feature"><svg viewBox="0 0 20 20"><circle cx="10" cy="10" r="9.5" fill="#111"/><path d="M5 12 L12 8 M5 9 L10 6 M8 14 L15 10" stroke="#fff" stroke-width="1.4"/></svg>Fast Dry Time</div>
          <div class="feature"><svg viewBox="0 0 20 20"><circle cx="10" cy="10" r="9.5" fill="#111"/><circle cx="10" cy="10" r="4" fill="none" stroke="#fff" stroke-width="1.6"/></svg>Scrub Resistant</div>
          <div class="feature"><svg viewBox="0 0 20 20"><circle cx="10" cy="10" r="9.5" fill="#111"/><path d="M10 4 L10 16 M5 8 L10 11 L15 8" fill="none" stroke="#fff" stroke-width="1.6"/></svg>Flexible Application</div>
          <div class="feature"><svg viewBox="0 0 20 20"><circle cx="10" cy="10" r="8.5" fill="none" stroke="#111" stroke-width="1.6"/><path d="M5 15 L15 5" stroke="#111" stroke-width="1.6"/></svg>Anti-Moulding effect</div>
          <div class="feature"><svg viewBox="0 0 20 20"><circle cx="10" cy="10" r="9.5" fill="#111"/><rect x="5" y="6" width="10" height="8" fill="none" stroke="#fff" stroke-width="1.5"/></svg>Long-Lasting Colour</div>
        </div>
      </div>
    </section>

    <section class="col col--mid">
      <div class="panel tools">
        <div class="wash" role="img" aria-label="Faint decorative background pattern"></div>
        <h2 class="h-blue">Application Tools</h2>
        <div class="tool-row">
          <div class="tool" style="left:76px; top:16px;"><svg viewBox="0 0 34 34"><circle cx="17" cy="17" r="16" fill="#111"/><path d="M10 24 L17 17 M15 15 L22 8 L26 12 L19 19Z" stroke="#fff" stroke-width="3" fill="#fff"/></svg>Brush</div>
          <div class="tool" style="left:226px; top:16px;"><svg viewBox="0 0 34 34"><circle cx="17" cy="17" r="16" fill="#111"/><rect x="12" y="8" width="14" height="8" transform="rotate(40 19 12)" fill="#fff"/><path d="M14 18 L9 26" stroke="#fff" stroke-width="2.5"/></svg>Roller</div>
          <div class="tool" style="left:148px; top:52px;"><svg viewBox="0 0 34 34"><circle cx="17" cy="17" r="16" fill="#111"/><rect x="13" y="11" width="8" height="16" rx="2" fill="#fff"/><rect x="15" y="7" width="4" height="4" fill="#fff"/></svg>Spray</div>
        </div>
      </div>
      <div class="panel condition">
        <div class="wash" role="img" aria-label="Faint decorative background pattern"></div>
        <h2 class="h-blue">Application condition</h2>
        <p>Surface must be clean, dry and free from dust, oils and grease.<br>Apply two coats ensuring that the first coat is completely dry before applying the second.</p>
      </div>
      <div class="panel instructions">
        <div class="wash" role="img" aria-label="Faint decorative background pattern"></div>
        <h2 class="h-blue">Application Instructions</h2>
        <ol class="steps">
          <li>1.&nbsp; Add 20% water in the paint, stir evenly in a circular lifting motion for before use</li>
          <li>2.&nbsp; Apply two coats on/in application tool</li>
          <li>3.&nbsp; Use primer[1] on dry wall and leave to dry</li>
          <li>4.&nbsp; Brush the wall with the paint as a finish (recommended two coats)</li>
          <li>5.&nbsp; Average dry time is 24 hours. If the weather is cold and wet, the dry time will be longer. Fully cured time is 7 days in summer, 15 days in winter.</li>
        </ol>
        <p class="remarks">Remarks<br>[1] If you don't have a primer product, you can use this paint as a primer.<br>In other words, the paint can be used as both a primer and finisher.</p>
      </div>
    </section>

    <section class="col col--right">
      <div class="panel care">
        <div class="wash" role="img" aria-label="Faint decorative background pattern"></div>
        <h3>During Painting</h3>
        <p>Ensure adequate ventilation. Keep floors and furniture covered</p>
        <h3>After Painting</h3>
        <p>Avoid exposure to steam for 48 hours Surface may be washed after 7 days</p>
        <h3>Coverage</h3>
        <p>Coverage Rate: Approx. 10m2/KG for 1 coat on wall<br>Approx. 5 m2/KG for 2 coat on wall</p>
        <h3>Disposal</h3>
        <p>Do not pour leftover paint in drains or sewers. Keep unwanted paint in sealed containers to be dispose via chemical waste collections. Unwanted paint can be brushed onto newspaper allowing time to dry then disposed via domestic waste collections.</p>
        <p class="warn">DO NOT REUSE CONTAINER UNLESS THOROUGHLY DECONTAMINATED</p>
      </div>
      <div class="panel safety">
        <div class="wash" role="img" aria-label="Faint decorative background pattern"></div>
        <h2>Safety and First Aid</h2>
        <h3>For spills and disposals:</h3>
        <p>Slippery when spilt, clean up immediately. Refer to Local Authority for disposal advice. Do not empty into drains and waterways.</p>
        <h3>First aid:</h3>
        <p>If poisoning occurs, contact a Doctor or Poison Help Line 130 555</p>
        <h3>Eye contact:</h3>
        <p>If contact is made with eyes, hold eyes open, flush with running water for at least 15 minutes.</p>
        <h3>Skin contact:</h3>
        <p>If contact is made with skin, remove any contaminated clothing and wash skin thoroughly.</p>
        <h3>If swallowed:</h3>
        <p>Rinse mouth with water, DO NOT induce vomiting</p>
        <h3>Clean up:</h3>
        <p>Wash up with water. Do not dispose of paint or wash water in drains or sewers</p>
        <p class="warn">ALWAYS KEEP OUT OF REACH OF CHILDREN</p>
      </div>
    </section>
  </div>

  <footer class="band band--bottom">
    <div class="band__cell"><span>Low Sheen</span><span>White</span><span>18L</span></div>
    <div class="band__cell"><span>Low Sheen</span><span>White</span><span>18L</span></div>
    <div class="band__cell"><span>Low Sheen</span><span>White</span><span>18L</span></div>
  </footer>
</main>
</body>
</html>
```